Real Estate Media Company Business Card

’m looking for a modern, high-end, double-sided business card for:
Brightpath Studio LLC
(Real Estate Photography & Videography)
The design should feel clean, minimal, and premium, appealing to top real estate agents and brokers.
👉 Horizontal layout is preferred
👉 Vertical option is welcome but not required
⸻
Front Side (Main Information):
Include:
* Tobias Wrenfield
* Brightpath Studio LLC
* Title (open to creative improvement)
* Phone Number
* Email
* Website
⸻
Services Section (VERY IMPORTANT):
This should be a key visual element, not an afterthought.
Services to Include:
* Cinematic Video
* Real Estate Photography
* Drone
* Social Media Reels
* Floor Plans
* Use clean, modern icons next to each service
* Icons should be simple, minimal, and consistent style (outline or thin line preferred)
* Option to place icons inside small circles (like reference)
Layout:
* Format services similar to a clean horizontal or grid-style list (like “example 2”)
* Keep spacing balanced and uncluttered
* Make this section visually appealing and easy to scan
⸻
Back Side:
* Keep it extremely minimal
* Only include the logo in a corner
* No additional text needed
⸻
Typography & Style:
* Modern, clean, slightly bold fonts (based on uploaded references)
* Strong hierarchy (name + services stand out most)
* Plenty of white/negative space
* Avoid clutter
⸻
Overall Feel:
* Luxury
* Modern
* Clean
* Confident
* High-end real estate branding
⸻
Notes for Designers:
* Simplicity is key
* Services section should feel polished and intentional
* This card should feel like something a top-producing real estate agent would keep
Real estate agent agents

```html
<!DOCTYPE html>
<html lang="en">
<head>
<meta charset="utf-8">
<title>Brightpath Studio LLC – Business Card</title>
<link rel="stylesheet" href="https://fonts.googleapis.com/css2?family=Ubuntu:wght@400;500;700&family=Montserrat:wght@400;500;700&display=swap">
<style>
  :root {
    --page-bg: #e6e7e9;
    --card-dark: #000000;
    --card-light: #ffffff;
    --ink-light: #ffffff;
    --ink-dark: #111111;
    --gold: #c79a2c;
    --rule-grey: #6b6b6b;
    --shadow: rgba(0, 0, 0, 0.22);
  }
  * { margin: 0; padding: 0; box-sizing: border-box; }
  html, body {
    width: 1200px; height: 1200px; overflow: hidden;
    background: var(--page-bg);
  }
  .card {
    position: absolute;
    left: 320px;
    width: 540px; height: 300px;
    border-radius: 25px;
    box-shadow: 14px 16px 22px var(--shadow);
    overflow: hidden;
  }
  .card--front { top: 283px; background: var(--card-dark); color: var(--ink-light); }
  .card--back { top: 603px; background: var(--card-light); color: var(--ink-dark); }

  .accent-bar {
    position: absolute; left: 33px; top: 26px;
    width: 32px; height: 3px; background: var(--gold);
  }
  .brand-name {
    position: absolute; left: 33px; top: 50px;
    font-family: "Montserrat", sans-serif; font-weight: 500;
    font-size: 15px; letter-spacing: 2px; color: var(--ink-light);
    white-space: nowrap;
  }
  .person-name {
    position: absolute; left: 33px; top: 104px;
    font-family: "Ubuntu", sans-serif; font-weight: 700;
    font-size: 27px; line-height: 1; white-space: nowrap;
  }
  .person-title {
    position: absolute; left: 33px; top: 136px;
    font-family: "Ubuntu", sans-serif; font-weight: 400;
    font-size: 15.5px; color: var(--gold); white-space: nowrap;
  }
  .title-rule {
    position: absolute; left: 33px; top: 167px;
    width: 32px; height: 2px; background: var(--gold);
  }
  .contact-list { list-style: none; }
  .contact-item {
    position: absolute; left: 33px;
    display: flex; align-items: center;
    font-family: "Ubuntu", sans-serif; font-size: 13.5px; white-space: nowrap;
  }
  .contact-item svg { width: 22px; height: 26px; margin-right: 15px; flex: none; }
  .contact-item--phone { top: 188px; }
  .contact-item--email { top: 220px; }
  .contact-item--web { top: 251px; }

  .column-divider {
    position: absolute; left: 309px; top: 48px;
    width: 1.5px; height: 204px; background: var(--gold);
  }
  .services-heading {
    position: absolute; left: 332px; top: 62px;
    font-family: "Montserrat", sans-serif; font-weight: 700;
    font-size: 16px; letter-spacing: 3.4px;
  }
  .service-list { list-style: none; }
  .service-item {
    position: absolute; left: 326px; width: 214px; height: 28px;
  }
  .service-item svg {
    position: absolute; left: 0; top: 0; width: 36px; height: 28px;
  }
  .service-tick {
    position: absolute; left: 367px; width: 1.5px; height: 22px; background: var(--gold);
  }
  .service-label {
    position: absolute; left: 60px; top: 7px;
    font-family: "Montserrat", sans-serif; font-weight: 500;
    font-size: 9.3px; letter-spacing: -0.1px; white-space: nowrap;
  }
  .service-rule {
    position: absolute; left: 363px; right: 0; height: 1px; background: var(--rule-grey);
  }

  .back-brand {
    position: absolute; left: 372px; top: 96px; width: 140px;
    text-align: center;
    font-family: "Montserrat", sans-serif; font-weight: 500;
    font-size: 17px; letter-spacing: 2px; line-height: 1.2; color: var(--ink-dark);
  }
</style>
</head>
<body>

<section class="card card--front" aria-label="Business card front">
  <div class="accent-bar"></div>
  <p class="brand-name">BRIGHTPATH STUDIO LLC</p>

  <h1 class="person-name">Tobias Wrenfield</h1>
  <p class="person-title">Founder &amp; Real Estate Media Specialist</p>
  <div class="title-rule"></div>

  <ul class="contact-list">
    <li class="contact-item contact-item--phone">
      <svg viewBox="0 0 22 26" fill="none" stroke="#fff" stroke-width="1.8">
        <rect x="5" y="1" width="12" height="24" rx="2"/>
        <line x1="9" y1="3.5" x2="13" y2="3.5"/>
      </svg>
      (555) 014 2290
    </li>
    <li class="contact-item contact-item--email">
      <svg viewBox="0 0 22 26" fill="none" stroke="#fff" stroke-width="1.6">
        <rect x="1" y="7" width="20" height="13"/>
        <polyline points="1,7 11,15 21,7"/>
        <line x1="1" y1="20" x2="8.5" y2="13"/>
        <line x1="21" y1="20" x2="13.5" y2="13"/>
      </svg>
      tobias@brightpathstudio.com
    </li>
    <li class="contact-item contact-item--web">
      <svg viewBox="0 0 22 26" fill="none" stroke="#fff" stroke-width="1.4">
        <circle cx="11" cy="13" r="10"/>
        <ellipse cx="11" cy="13" rx="4.5" ry="10"/>
        <line x1="11" y1="3" x2="11" y2="23"/>
        <line x1="1" y1="13" x2="21" y2="13"/>
        <path d="M3 8 H19 M3 18 H19"/>
      </svg>
      brightpathstudio.com
    </li>
  </ul>

  <div class="column-divider"></div>

  <h2 class="services-heading">SERVICES</h2>
  <ul class="service-list">
    <li class="service-item" style="top:95px">
      <svg viewBox="0 0 36 28" fill="none" stroke="#fff" stroke-width="1.5">
        <rect x="6" y="8" width="25" height="17" rx="2"/>
        <path d="M13 8 L15 4 H22 L24 8"/>
        <circle cx="18.5" cy="16.5" r="5.5"/>
        <circle cx="18.5" cy="16.5" r="3"/>
      </svg>
      <span class="service-label">REAL ESTATE PHOTOGRAPHY</span>
    </li>
    <li class="service-item" style="top:126px">
      <svg viewBox="0 0 36 28" fill="none" stroke="#fff" stroke-width="1.5">
        <circle cx="12" cy="6" r="4"/>
        <circle cx="20" cy="6" r="4"/>
        <rect x="6" y="11" width="20" height="15" rx="2"/>
        <rect x="9" y="16" width="10" height="6"/>
        <polygon points="26,16 32,12 32,25 26,21"/>
      </svg>
      <span class="service-label">CINEMATIC VIDEO</span>
    </li>
    <li class="service-item" style="top:157px">
      <svg viewBox="0 0 36 28" fill="none" stroke="#fff" stroke-width="1.6">
        <line x1="1" y1="5" x2="11" y2="5"/>
        <line x1="25" y1="5" x2="35" y2="5"/>
        <line x1="6" y1="3" x2="6" y2="9"/>
        <line x1="30" y1="3" x2="30" y2="9"/>
        <path d="M6 9 L13 13 H23 L30 9"/>
        <path d="M13 13 Q18 7 23 13" fill="#fff"/>
        <path d="M11 20 L14 14 M25 20 L22 14"/>
        <rect x="15" y="18" width="6" height="6" rx="1" fill="#fff"/>
      </svg>
      <span class="service-label">SCOPE DRONE / AERIAL</span>
    </li>
    <li class="service-item" style="top:188px">
      <svg viewBox="0 0 36 28" fill="none" stroke="#fff" stroke-width="1.5">
        <path d="M6 4 Q6 1 9 1 V24 Q6 24 6 27 Z"/>
        <rect x="9" y="3" width="21" height="23"/>
        <rect x="12" y="6" width="15" height="17"/>
        <path d="M18 6 V12 M18 15 V23 M18 14 H27 M12 14 H15"/>
      </svg>
      <span class="service-label">FLOOR PLAN</span>
    </li>
    <li class="service-item" style="top:219px">
      <svg viewBox="0 0 36 28" fill="none" stroke="#fff" stroke-width="1.5">
        <polyline points="4,13 18,2 32,13"/>
        <polyline points="7,12 7,27 29,27 29,12"/>
        <rect x="12" y="18" width="12" height="6" rx="1"/>
        <path d="M14 18 V14 H22 V18"/>
      </svg>
      <span class="service-label">VIRTUAL STAGING</span>
    </li>
  </ul>
  <div class="service-tick" style="top:95px"></div>
  <div class="service-tick" style="top:126px"></div>
  <div class="service-tick" style="top:157px"></div>
  <div class="service-tick" style="top:188px"></div>
  <div class="service-tick" style="top:219px"></div>
  <div class="service-rule" style="top:121px"></div>
  <div class="service-rule" style="top:151px"></div>
  <div class="service-rule" style="top:181px"></div>
  <div class="service-rule" style="top:212px"></div>
</section>

<section class="card card--back" aria-label="Business card back">
  <p class="back-brand">BRIGHTPATH STUDIO</p>
</section>

</body>
</html>
```